Business Card & Letterhead Design

We a financial advice company based in Australia. We provide advice to wealthy farmers.

We are changing our business name FROM Brightmere Financial TO Calderstone Wealth and we need a new letterhead and double sided business card design

Attached is designs from our previous branding (Brightmere Financial) as it includes all the details we require on the new Calderstone Wealth business cards and letterhead.

```html
<!DOCTYPE html>
<html lang="en">
<head>
<meta charset="utf-8">
<title>Calderstone Wealth Stationery</title>
<link href="https://fonts.googleapis.com/css2?family=Arimo:wght@400;700&family=Open+Sans:wght@400;600;700&display=swap" rel="stylesheet">
<style>
:root{
  --backdrop:#e4e4e4;
  --paper:#f5f5f5;
  --ink:#3a3a3a;
  --ink-soft:#555;
  --slate:#5a6670;
  --charcoal:#444;
  --white:#fff;
}
*{margin:0;padding:0;box-sizing:border-box}
html,body{width:1200px;height:1200px;overflow:hidden;background:var(--backdrop)}
.sheet-area{position:relative;width:1200px;height:1200px}
.letterhead{position:absolute;left:117px;top:138px;width:654px;height:925px;background:var(--paper);font-family:"Arimo",Arial,sans-serif;color:var(--ink)}
.brand{position:absolute;font-family:"Open Sans",sans-serif;color:var(--ink);font-weight:400;white-space:nowrap}
.brand-circle{position:absolute;border:2.5px solid var(--ink);border-radius:50%}
.lh-circle{left:123px;top:38px;width:54px;height:54px}
.lh-name{left:50px;top:96px;width:200px;text-align:center;font-size:17px;letter-spacing:.5px;text-transform:uppercase}
.lh-info{position:absolute;font-family:"Open Sans",sans-serif;font-size:8.6px;line-height:11.2px;color:var(--ink-soft)}
.col-a{left:311px}
.col-b{left:477px}
.info-top{top:33px}
.info-bottom{top:77px}
.lh-rule{position:absolute;left:311px;right:0;top:73px;border-top:1px solid var(--ink-soft)}
.icon{display:inline-block;width:8px;height:8px;vertical-align:-1px;margin-right:2px}
.letter-date{position:absolute;left:50px;top:188px;font-size:10px}
.recipient{position:absolute;left:50px;top:215px;font-size:10px;line-height:13.2px}
.salutation{position:absolute;left:50px;top:307px;font-size:10px;font-weight:700}
.letter-body{position:absolute;left:50px;top:346px;width:554px;font-size:9.9px;line-height:13.2px;text-align:justify}
.letter-body p{margin-bottom:13px}
.closing{position:absolute;left:50px;top:637px;font-size:10px}
.signature{position:absolute;left:50px;top:668px;width:170px;height:22px;background:#e7e7e7}
.signatory{position:absolute;left:50px;top:703px;font-size:10px;line-height:13.2px}
.licence-note{position:absolute;left:0;width:654px;top:858px;text-align:center;font-family:"Open Sans",sans-serif;font-size:8.6px;line-height:11px;color:var(--ink-soft)}
.tag-band{position:absolute;left:0;bottom:0;width:100%;height:31px;background:linear-gradient(90deg,var(--charcoal) 0%,var(--charcoal) 45%,var(--slate) 60%,var(--slate) 100%);font-family:"Open Sans",sans-serif;font-weight:600;color:var(--white);font-size:10px;white-space:nowrap}
.tag-left{position:absolute;right:354px;top:8px}
.tag-right{position:absolute;left:352px;top:8px}
.band-circle{position:absolute;border:1.5px solid var(--white);border-radius:50%}
.lh-band-circle{left:312px;top:1px;width:30px;height:30px}

.card{position:absolute;left:805px;width:280px;height:171px;font-family:"Open Sans",sans-serif}
.card-front{top:212px;background:var(--slate);color:var(--white)}
.cf-circle{position:absolute;left:72px;top:42px;width:30px;height:30px;border:2px solid var(--white);border-radius:50%}
.cf-name{position:absolute;left:22px;top:80px;width:130px;text-align:center;font-size:7px;letter-spacing:.3px;text-transform:uppercase;color:var(--white);white-space:nowrap}
.cf-divider{position:absolute;left:160px;top:54px;height:58px;border-left:1px solid var(--white)}
.services{position:absolute;left:172px;top:58px;list-style:none;font-size:6.8px;line-height:13px;text-transform:uppercase}
.cf-licence{position:absolute;left:0;top:140px;width:100%;text-align:center;font-size:6.8px;line-height:9.3px}
.card-back{top:439px;background:var(--paper);color:var(--ink-soft)}
.cb-circle{position:absolute;left:191px;top:14px;width:30px;height:30px;border:2px solid var(--ink);border-radius:50%}
.cb-name{position:absolute;right:17px;top:45px;font-size:10.5px;letter-spacing:.3px;text-transform:uppercase;color:var(--ink);white-space:nowrap}
.person{position:absolute;left:17px;top:75px;font-size:6.8px;line-height:9.3px}
.person strong{font-size:8.8px;font-weight:600;color:var(--ink)}
.person .cred{font-size:6.2px;font-weight:600;color:var(--ink)}
.cb-rule{position:absolute;left:103px;right:17px;top:102px;border-top:1px solid var(--ink-soft)}
.cb-address{position:absolute;left:17px;top:115px;font-size:6.8px;line-height:9.3px}
.cb-contact{position:absolute;right:17px;top:106px;text-align:right;font-size:6.8px;line-height:9.3px}
.cb-contact .icon{width:6px;height:6px;margin:0 0 0 2px;vertical-align:-.5px}
.cb-band{position:absolute;left:0;bottom:0;width:100%;height:13px;background:linear-gradient(90deg,var(--charcoal) 0%,var(--charcoal) 45%,var(--slate) 60%,var(--slate) 100%);color:var(--white);font-size:6.6px;font-weight:600;white-space:nowrap}
.cb-band .tag-left{right:auto;left:17px;top:1.5px}
.cb-band .tag-right{left:auto;right:17px;top:1.5px}
.cb-band-circle{left:133px;top:0;width:13px;height:13px;border-width:1px}
</style>
</head>
<body>
<div class="sheet-area">

<section class="letterhead">
  <span class="brand-circle lh-circle"></span>
  <span class="brand lh-name">Calderstone Wealth</span>

  <div class="lh-info col-a info-top">Halvorne Investments Pty Ltd<br>Corporate Authorised Representative<br>of Westbury Financial Planning Limited</div>
  <div class="lh-info col-b info-top">ATF The Ashgrove Investment Trust<br>T/AS Brightmere Financial<br>ABN: 41 208 375 912</div>
  <div class="lh-rule"></div>
  <div class="lh-info col-a info-bottom">Suite 4A, 18 Harlow St<br>Riverside QLD 4101<br>PO Box 5120<br>Eastfield QLD 4101</div>
  <div class="lh-info col-b info-bottom">
    <svg class="icon" viewBox="0 0 10 10"><path d="M2 1l2 2-1 1.2c.6 1.3 1.5 2.2 2.8 2.8L7 6l2 2-1.3 1.3C4.5 9 1 5.5.7 2.3z" fill="#555"/></svg>(07) 3010 2480<br>
    <svg class="icon" viewBox="0 0 10 10"><rect x="2.5" y="1" width="5" height="3" fill="#555"/><rect x="1" y="4" width="8" height="4" fill="#555"/><rect x="2.5" y="7" width="5" height="2.5" fill="#fff" stroke="#555"/></svg>(07) 3010 2481<br>
    <svg class="icon" viewBox="0 0 10 10"><rect x="1" y="2" width="8" height="6" fill="none" stroke="#555"/><path d="M1 2l4 3.5L9 2" fill="none" stroke="#555"/></svg>admin@calderstonewealth.com.au<br>
    <svg class="icon" viewBox="0 0 10 10"><circle cx="5" cy="5" r="4" fill="none" stroke="#555"/><ellipse cx="5" cy="5" rx="1.8" ry="4" fill="none" stroke="#555"/><path d="M1 5h8" stroke="#555"/></svg>www.calderstonewealth.com.au
  </div>

  <div class="letter-date">September 25, 2019</div>
  <div class="recipient">Mr. John Doe<br>President<br>AA Corporation<br>111 Street Name, Suite#<br>City, State, 12345</div>
  <div class="salutation">Dear Mr. John,</div>

  <div class="letter-body">
    <p>Lorem ipsum dolor sit amet, consectetur adipiscing elit. Integer diam quam, egestas eu ultrices eu, suscipit ac sapien. Phasellus eu dui nisi. Nam et euismod diam, nec lobortis tortor. Donec et diam nulla. Aenean varius tincidunt convallis. Aliquam a tortor at lacus dictum aliquet. Nunc laoreet metus sapien, in scelerisque augue consectetur in.</p>
    <p>Fusce nec justo laoreet, egestas justo sed, aliquet sem. Pellentesque pharetra massa non orci bibendum semper. Pellentesque cursus eu lectus a consectetur. Nunc volutpat suscipit posuere. Vestibulum facilisis vel quam malesuada mattis. Nulla in mattis tellus. Maecenas tristique mauris vitae pharetra tincidunt. In ut ornare risus. Integer molestie vestibulum nisi, semper dapibus mi condimentum eu.</p>
    <p>Nullam sagittis elit libero, id fringilla est tincidunt eget. Donec in ipsum ultricies, consectetur quam vel, facilisis elit. Phasellus tincidunt congue risus vel luctus. Suspendisse ut mollis neque. Donec ornare orci in turpis vestibulum, in ultrices metus scelerisque. Pellentesque mattis mattis nunc, nec tincidunt lacus egestas id. Fusce facilisis sagittis neque sit amet vulputate. Aliquam ut eros lobortis tortor facilisis vehicula. Sed sed luctus leo, at laoreet sapien. Donec placerat adipiscing ligula non euismod. In lobortis pretium nisl id luctus.</p>
    <p>Integer gravida tincidunt nibh, scelerisque tincidunt turpis. Suspendisse potenti. Nunc hendrerit euismod lectus id elementum. Fusce vitae gravida velit, quis eleifend lectus. In imperdiet mauris eu dui viverra sagittis. Donec tempor dui diam, condimentum gravida lacus pretium a. Nullam fringilla augue quis arcu placerat scelerisque. Aliquam nec tincidunt augue, sit amet posuere ipsum.</p>
  </div>

  <div class="closing">Sincerely Yours,</div>
  <div class="signature" role="img" aria-label="Handwritten signature of Daniel Marsh"></div>
  <div class="signatory">Daniel Marsh<br>President</div>

  <div class="licence-note">Westbury Financial Planning Limited ABN 62 115 804 337 &nbsp;|&nbsp; Australian Financial Services Licence Licence Number 318 204<br>Principle Address: 120 Market St PO Box 1140 Melbourne VIC 3000</div>

  <div class="tag-band">
    <span class="tag-left">A RELATIONSHIP LED PRACTICE</span>
    <span class="band-circle lh-band-circle"></span>
    <span class="tag-right">CLARITY FOR EVERY SEASON</span>
  </div>
</section>

<section class="card card-front">
  <span class="cf-circle"></span>
  <span class="cf-name">Calderstone Wealth</span>
  <div class="cf-divider"></div>
  <ul class="services">
    <li>Life &amp; TPD Insurance</li>
    <li>Income Protection</li>
    <li>Financial Planning</li>
    <li>Retirement Planning</li>
  </ul>
  <div class="cf-licence">Westbury Financial Planning Limited<br>Australian Financial Services Licensee Licence Number 318 204</div>
</section>

<section class="card card-back">
  <span class="cb-circle"></span>
  <span class="cb-name">Calderstone Wealth</span>
  <div class="person"><strong>Tom Hadley</strong> <span class="cred">B.Ag.Ec. Dip F.P. CFP®</span><br>Managing Director<br>Authorised Representative</div>
  <div class="cb-rule"></div>
  <div class="cb-address">Suite 4A, 18 Harlow St<br>Riverside QLD 4101<br>PO Box 5120<br>Eastfield QLD 4101</div>
  <div class="cb-contact">
    (07) 3010 2480<svg class="icon" viewBox="0 0 10 10"><path d="M2 1l2 2-1 1.2c.6 1.3 1.5 2.2 2.8 2.8L7 6l2 2-1.3 1.3C4.5 9 1 5.5.7 2.3z" fill="#555"/></svg><br>
    0412 508 336<svg class="icon" viewBox="0 0 10 10"><rect x="2.5" y=".5" width="5" height="9" rx="1" fill="none" stroke="#555"/></svg><br>
    (07) 3010 2481<svg class="icon" viewBox="0 0 10 10"><rect x="2.5" y="1" width="5" height="3" fill="#555"/><rect x="1" y="4" width="8" height="4" fill="#555"/></svg><br>
    tom@calderstonewealth.com.au<svg class="icon" viewBox="0 0 10 10"><rect x="1" y="2" width="8" height="6" fill="none" stroke="#555"/><path d="M1 2l4 3.5L9 2" fill="none" stroke="#555"/></svg><br>
    www.calderstonewealth.com.au<svg class="icon" viewBox="0 0 10 10"><circle cx="5" cy="5" r="4" fill="none" stroke="#555"/><path d="M1 5h8" stroke="#555"/></svg>
  </div>
  <div class="cb-band">
    <span class="tag-left">A RELATIONSHIP LED PRACTICE</span>
    <span class="band-circle cb-band-circle"></span>
    <span class="tag-right">CLARITY FOR EVERY SEASON</span>
  </div>
</section>

</div>
</body>
</html>
```